Label for new gin: Kliff7 - Distilled Gin

Artistic label with local elements for new gin brand.
Dunes, lighthouses, sea, seagulls, ships.
Fresh lemon gin with fine juniper notes. Manufactured directly on the Baltic Sea in Warnemünde. Should be scalable. 4x6inch or larger.
Motifs put together artistically. Photos of the place in the attachment. The name of the gin comes from the beach entrance 3 (hence dune 3). A dune stalk (blue oat) is in the bottle. Bottle will be a clear glass apothecary bottle 500ml.
Updates

Niedrige Design-Qualität

Target Market(s)

spirits

Industry/Entity Type

Getränke

Font styles to use
Decorative
Script

Colors

Designer to choose colors to be used in the design.

Requirements
Must have
• Sketch, Handdrawn Style /// 500ml, 41% vol Alc "Made by QMTO GmbH Farnstieg 22a Roggentin" "Bottled in Warnemünde" "Kliff7" "Distilled Gin" "Inspired by the sea"

```html
<!DOCTYPE html>
<html lang="en">
<head>
<meta charset="utf-8">
<title>Kliff7 Distilled Gin – Label</title>
<link rel="stylesheet" href="https://fonts.googleapis.com/css2?family=EB+Garamond&family=Oswald:wght@400;600&family=Playfair+Display:wght@700&family=Rochester&family=Cormorant+Garamond:ital@1&display=swap">
<style>
  :root {
    --page: #ffffff;
    --label: #f5f5f5;
    --gold: #d3920c;
    --navy: #1c2140;
    --sketch-light: #eef0f4;
    --sketch-dark: #c9ccd6;
  }
  * { margin: 0; padding: 0; box-sizing: border-box; }
  html, body {
    width: 1200px; height: 800px; overflow: hidden;
    background: var(--page);
  }
  .canvas { position: relative; width: 1200px; height: 800px; }
  .label {
    position: absolute; left: 379px; top: 72px;
    width: 433px; height: 653px;
    background: var(--label);
    box-shadow: 1px 2px 3px rgba(0,0,0,0.25);
  }
  .label > * { position: absolute; }
  .bracket-frame { left: 45px; top: 50px; width: 340px; height: 82px; overflow: visible; }
  .bottled-in {
    left: 0; width: 100%; top: 28px; text-align: center;
    font-family: "Rochester", cursive;
    font-size: 30px; color: var(--gold);
    transform: rotate(-2deg);
  }
  .coast-scene {
    left: 18px; top: 76px; width: 413px; height: 140px;
    background: linear-gradient(180deg, var(--label) 0%, var(--sketch-light) 45%, var(--sketch-dark) 100%);
  }
  .info-box {
    left: 39px; top: 214px; width: 354px; height: 337px;
    border: 2px solid var(--navy);
  }
  .tagline {
    left: 0; width: 100%; top: 226px; text-align: center;
    font-family: "Oswald", sans-serif; font-weight: 600;
    font-size: 20px; letter-spacing: 1px; color: var(--gold);
  }
  .brand-name {
    left: 20px; width: 400px; top: 262px; text-align: center;
    font-family: "Playfair Display", serif; font-weight: 700;
    font-size: 140px; line-height: 1; color: var(--gold);
  }
  .product-type {
    left: 0; width: 100%; top: 440px; text-align: center; padding-left: 90px;
    font-family: "Oswald", sans-serif; font-weight: 400;
    font-size: 28px; color: var(--navy);
  }
  .maker {
    left: 0; width: 100%; top: 526px; text-align: center;
    font-family: "Cormorant Garamond", serif; font-style: italic;
    font-size: 11px; letter-spacing: 1.5px; color: var(--navy);
  }
  .volume {
    left: 0; width: 100%; top: 578px; text-align: center;
    font-family: "EB Garamond", serif;
    font-size: 24px; color: var(--navy);
  }
</style>
</head>
<body>
<main class="canvas">
  <section class="label">
    <svg class="bracket-frame" viewBox="0 0 340 82" aria-hidden="true">
      <polyline points="2,82 2,2 30,1" fill="none" stroke="var(--gold)" stroke-width="2"/>
      <polyline points="310,3 339,3 339,56" fill="none" stroke="var(--gold)" stroke-width="2"/>
    </svg>
    <p class="bottled-in">Bottled in Warnemünde</p>
    <div class="coast-scene" role="img" aria-label="Hand-drawn sketch of Warnemünde: seagulls on rocks, two lighthouses, the curved Teepott building and beach grass"></div>
    <div class="info-box"></div>
    <p class="tagline">INSPIRED BY THE SEA</p>
    <h1 class="brand-name">Kliff7</h1>
    <p class="product-type">DISTILLED GIN</p>
    <p class="maker">Made by QMTO GmbH Farnstieg 22a Roggentin</p>
    <p class="volume">500ml, 41% vol Alc</p>
  </section>
</main>
</body>
</html>
```